Unique Beautiful Realtor business card

I need a unique business card that includes my logo, my firms logo, my picture and phone number. The colors should compliment my logo.

Target Market(s)

People who want to buy or sell a home in South Florida

Contact Information for Business Card

Use two sides and work with the TMQ Coastal Dwellings logo as a theme.
The Dorsett Ambrose should be small and discreet, it is a requirement to be there but should be small. My photo should be integrated artistically.

Font styles to use
Serif
Sans Serif

Colors

Designer to choose colors to be used in the design.

Requirements
Must have
• My logo, Dorsett Ambrose logo, my photo, my phone number, (555-203-8846) and my website address. (www.tmqcoastaldwellings.example)
• Also my name, Marla J. Quenby, PA, Realtor
• Also “The Garden Minded Realtor”

```html
<!DOCTYPE html>
<html lang="en">
<head>
<meta charset="utf-8">
<title>Marla J. Quenby – Business Card</title>
<link href="https://fonts.googleapis.com/css2?family=Montserrat:wght@600;700&family=Open+Sans:ital,wght@0,400;0,600;1,600&display=swap" rel="stylesheet">
<style>
  :root{
    --bg:#2a2c30;
    --white:#ffffff;
    --navy:#0d4a8c;
    --navy-dark:#123a66;
    --lime:#a8b62e;
    --sun:#f6c21c;
    --ink:#2f3238;
    --grey:#6b6e73;
  }
  *{box-sizing:border-box;margin:0;padding:0}
  html,body{width:1200px;height:900px;overflow:hidden;background:var(--bg)}
  body{font-family:"Open Sans",Arial,sans-serif;position:relative}

  .card{
    position:absolute;left:290px;width:620px;height:354px;
    background:var(--white);border-radius:22px;overflow:hidden;
  }
  .card--front{top:62px}
  .card--back{top:484px}

  /* front */
  .front-band{position:absolute;left:0;right:0;top:150px;height:176px;background:var(--navy)}
  .front-edge{position:absolute;left:0;right:0;bottom:0;height:28px;background:var(--lime)}
  .brand{
    position:absolute;left:90px;top:112px;width:440px;height:76px;
    background:var(--white);border:4px solid var(--lime);
    display:flex;align-items:center;justify-content:center;gap:14px;
  }
  .brand-dot{width:26px;height:26px;border-radius:50%;background:var(--sun);flex:none}
  .brand-name{
    font-family:"Montserrat",Arial,sans-serif;font-weight:700;font-size:23px;
    letter-spacing:1px;color:var(--navy-dark);text-transform:uppercase;white-space:nowrap;
  }
  .tagline{
    position:absolute;left:0;right:0;top:222px;
    display:flex;align-items:center;justify-content:center;gap:16px;
    color:var(--white);font-style:italic;font-weight:600;font-size:19px;
  }
  .tagline::before,.tagline::after{content:"";width:80px;height:2px;background:var(--white)}

  /* back */
  .portrait{
    position:absolute;left:0;top:0;width:250px;height:236px;
    background:linear-gradient(160deg,#9fb7a2 0%,#6f8a74 35%,#4a4d55 65%,#8d98a6 100%);
  }
  .portrait::after{content:"";position:absolute;right:0;top:0;bottom:0;width:70px;
    background:linear-gradient(90deg,rgba(255,255,255,0),var(--white))}
  .portrait::before{content:"";position:absolute;left:0;right:0;bottom:0;height:50px;
    background:linear-gradient(180deg,rgba(255,255,255,0),var(--white))}
  .back-edge{position:absolute;left:0;right:0;bottom:0;height:42px;background:var(--lime)}
  .details{position:absolute;left:272px;top:40px;right:20px}
  .agent-name{font-family:"Montserrat",Arial,sans-serif;font-weight:700;font-size:22px;color:var(--navy);text-transform:uppercase;letter-spacing:.3px;white-space:nowrap}
  .agent-title{font-size:17px;color:var(--ink);margin-top:2px}
  .services{font-size:15px;font-weight:600;font-style:italic;color:var(--navy);margin:10px 0 12px}
  .contact{list-style:none}
  .contact li{display:flex;align-items:center;gap:10px;font-size:16px;color:var(--ink);line-height:28px;white-space:nowrap}
  .contact svg{width:18px;height:18px;flex:none}
  .firm{
    position:absolute;left:30px;bottom:60px;display:flex;align-items:center;gap:8px;
    font-size:14px;font-weight:600;color:var(--grey);text-transform:uppercase;letter-spacing:.5px;white-space:nowrap;
  }
  .firm-mark{width:14px;height:14px;background:var(--grey)}
</style>
</head>
<body>

<section class="card card--front" aria-label="Card front">
  <div class="front-band"></div>
  <div class="front-edge"></div>
  <div class="brand">
    <span class="brand-dot"></span>
    <span class="brand-name">TMQ Coastal Dwellings</span>
  </div>
  <p class="tagline">The Garden Minded Realtor</p>
</section>

<section class="card card--back" aria-label="Card back">
  <div class="portrait" role="img" aria-label="Photo of the realtor outdoors by the water"></div>
  <div class="back-edge"></div>
  <div class="details">
    <h1 class="agent-name">Marla J. Quenby, PA</h1>
    <p class="agent-title">Realtor®</p>
    <p class="services">Buying • Selling • Investment</p>
    <ul class="contact">
      <li>
        <svg viewBox="0 0 24 24" aria-hidden="true"><path fill="#a8b62e" d="M6.6 10.8a15 15 0 006.6 6.6l2.2-2.2a1 1 0 011-.25 11.4 11.4 0 003.6.57 1 1 0 011 1V20a1 1 0 01-1 1A17 17 0 013 4a1 1 0 011-1h3.5a1 1 0 011 1c0 1.25.2 2.45.57 3.57a1 1 0 01-.25 1z"/></svg>
        555-203-8846
      </li>
      <li>
        <svg viewBox="0 0 24 24" aria-hidden="true"><rect x="2" y="5" width="20" height="14" rx="1" fill="#a8b62e"/><path d="M3 6l9 7 9-7" fill="none" stroke="#fff" stroke-width="1.6"/></svg>
        marla@tmqcoastaldwellings.example
      </li>
      <li>
        <svg viewBox="0 0 24 24" aria-hidden="true"><circle cx="12" cy="12" r="9.5" fill="none" stroke="#a8b62e" stroke-width="2"/><path d="M2.5 12h19M12 2.5c3 3 3 16 0 19M12 2.5c-3 3-3 16 0 19" fill="none" stroke="#a8b62e" stroke-width="1.6"/></svg>
        www.tmqcoastaldwellings.example
      </li>
    </ul>
  </div>
  <div class="firm"><span class="firm-mark"></span>Dorsett Ambrose · Palm Hollow</div>
</section>

</body>
</html>
```